Ginger Beer Can Design for a none alcoholic bavarage

We need a cool, modern, fresh design for a can.

- 330ml sleek can size
- 0.0% alcohol
- BIO
- ingredience: Water, Sugar, Ginger, limejuice, Gummi Arabicum, Carbonisation
- Energy table of fats, carbs, protein, etc.
- address: Quiet Meadow Drinks, Lindenweg 42, 4052 Basel

```html
<!DOCTYPE html>
<html lang="en">
<head>
<meta charset="utf-8">
<title>Quiet Meadow Drinks – Ginger &amp; Lime Can Label</title>
<link href="https://fonts.googleapis.com/css2?family=Alfa+Slab+One&family=Montserrat:wght@600;700;800&display=swap" rel="stylesheet">
<style>
  :root{
    --lime-yellow:#f4ec12;
    --lime-green:#7fcf3a;
    --leaf-green:#4cbd45;
    --ink:#0d0d0d;
    --text-dark:#173312;
    --white:#ffffff;
    --pill-yellow:#f6ea1a;
    --page:#ffffff;
  }
  *{margin:0;padding:0;box-sizing:border-box}
  html,body{width:1200px;height:2456px;overflow:hidden;background:var(--page)}
  body{position:relative;font-family:"Montserrat",sans-serif}
  .label{
    position:absolute;left:64px;top:823px;width:1072px;height:810px;
    overflow:hidden;box-shadow:0 6px 18px rgba(0,0,0,.18);
  }
  .label-bg{position:absolute;inset:0}
  .abs{position:absolute}
  .brand-tab{
    left:200px;top:0;width:220px;height:280px;background:var(--ink);
    border-radius:0 0 110px 110px;display:flex;flex-direction:column;
    align-items:center;justify-content:center;gap:14px;
  }
  .brand-dot{width:22px;height:22px;border-radius:50%;background:var(--white)}
  .brand-name{
    color:var(--white);font-weight:800;font-size:24px;line-height:1.15;
    text-align:center;text-transform:uppercase;letter-spacing:1px;
  }
  .product-title{
    left:150px;top:318px;width:320px;text-align:center;
    font-family:"Alfa Slab One",serif;font-style:italic;color:var(--white);
    font-size:62px;line-height:58px;text-shadow:3px 3px 0 var(--ink);
  }
  .pill{display:inline-block;font-weight:700;border-radius:6px;white-space:nowrap}
  .tagline{
    left:178px;top:466px;background:var(--pill-yellow);color:var(--ink);
    font-size:19px;padding:5px 14px;
  }
  .alcohol{
    left:322px;top:538px;background:var(--white);color:var(--ink);
    font-size:17px;padding:4px 12px;border-radius:16px;font-weight:600;
  }
  .fruit-photo{
    left:190px;top:585px;width:250px;height:165px;border-radius:40%;
    background:radial-gradient(circle at 45% 45%,#f3d64a,#d9a85a 60%,#6f8d3a);
  }
  .organic{
    left:128px;top:664px;color:var(--white);font-weight:800;font-size:14px;line-height:13px;
  }
  .volume{left:280px;top:775px;color:var(--pill-yellow);font-weight:700;font-size:17px}
  .info-pill{background:var(--white);color:var(--ink);font-size:19px;padding:5px 14px;border-radius:4px}
  .ingredients-head{left:572px;top:60px}
  .ingredients{
    left:585px;top:112px;color:var(--text-dark);font-weight:600;font-size:19px;line-height:25px;
  }
  .nutrition{
    left:572px;top:267px;width:389px;border-collapse:collapse;color:var(--text-dark);
    font-size:19px;font-weight:600;
  }
  .nutrition th,.nutrition td{border:1.5px solid var(--ink);height:44px;padding:0 14px}
  .nutrition th{background:var(--white);color:var(--ink);font-weight:800;text-align:left;font-size:18px}
  .nutrition td.value,.nutrition th.value{text-align:center;width:148px}
  .maker-head{left:572px;top:680px}
  .maker{left:585px;top:730px;color:var(--text-dark);font-weight:800;font-size:19px;line-height:24px}
  .maker-address{font-weight:700}
  .lemon-slice{left:950px;top:0;width:122px;height:130px;border-radius:0 0 0 70px;
    background:radial-gradient(circle at 70% 30%,#fff7a0,#f2e416 70%)}
  .leaf-art{left:975px;top:690px;width:80px;height:100px;border-radius:70% 0 70% 0;background:var(--white)}
</style>
</head>
<body>
<section class="label">
  <svg class="label-bg" width="1072" height="810" viewBox="0 0 1072 810" aria-hidden="true">
    <defs>
      <linearGradient id="labelGradient" gradientUnits="userSpaceOnUse" x1="0" y1="0" x2="900" y2="810">
        <stop offset="0" stop-color="#f7ef10"/>
        <stop offset=".35" stop-color="#a6d637"/>
        <stop offset=".6" stop-color="#5cc244"/>
        <stop offset=".8" stop-color="#c8e22a"/>
        <stop offset="1" stop-color="#f0ea14"/>
      </linearGradient>
    </defs>
    <rect width="1072" height="810" fill="#0d0d0d"/>
    <rect width="620" height="810" fill="url(#labelGradient)"/>
    <ellipse cx="520" cy="410" rx="560" ry="570" fill="url(#labelGradient)"/>
    <path d="M60 810 L80 740 L105 680 L150 625 L230 580 L330 545 L450 515 L545 490 L515 545 L475 585 L465 660 L440 720 L390 780 L350 810 Z" fill="#0d0d0d"/>
  </svg>

  <div class="abs lemon-slice" role="img" aria-label="Lemon slice illustration"></div>

  <div class="abs brand-tab">
    <span class="brand-dot"></span>
    <span class="brand-name">Quiet Meadow<br>Drinks</span>
  </div>

  <h1 class="abs product-title">GINGER<br>&amp; LIME</h1>
  <span class="abs pill tagline">SPARKLING INFUSION</span>
  <span class="abs pill alcohol">0.0% Alcohol</span>

  <div class="abs fruit-photo" role="img" aria-label="Photo of lemons, lemon halves and ginger root with leaves"></div>
  <p class="abs organic">100%<br>ORGANIC</p>
  <p class="abs volume">330ml</p>

  <span class="abs pill info-pill ingredients-head">INGREDIENCE:</span>
  <p class="abs ingredients">Water, Sugar, Ginger,<br>limejuice, Gummi Arabicum,<br>Carbonisation.</p>

  <table class="abs nutrition">
    <thead><tr><th>NUTRITIONAL DATA</th><th class="value">PER 100ML</th></tr></thead>
    <tbody>
      <tr><td>Energy</td><td class="value">00</td></tr>
      <tr><td>Fat</td><td class="value">00</td></tr>
      <tr><td>Carbohydrates</td><td class="value">00</td></tr>
      <tr><td>Protein</td><td class="value">00</td></tr>
      <tr><td>Salt</td><td class="value">00</td></tr>
    </tbody>
  </table>

  <span class="abs pill info-pill maker-head">MANUFACTURED BY:</span>
  <p class="abs maker">QUIET MEADOW DRINKS<br><span class="maker-address">Lindenweg 42, 4052 Basel</span></p>

  <div class="abs leaf-art" role="img" aria-label="White leaf illustration"></div>
</section>
</body>
</html>
```